Real Estate Business Cards

Looking for a clean, sharp and professional look for our Real Estate investment Fund that invests in Multi Family Apartment buildings.

Target Market(s)

Real Estate Fund

Industry/Entity Type

Real Estate

Contact Information for Business Card

Company Description: Real Estate Investment Fund
Company Name: RKW Holdings
Name: Marcus Olvane
Cell: (917) 482-0657
Email: marcus@rkwholdings-example.com
Website: www.rkwholdings-example.com
Address: 418, 9th Street, Brooklyn NY 11218

Colors

Designer to choose colors to be used in the design.

Requirements
Nice to have
• Colors to match logo

```html
<!DOCTYPE html>
<html lang="en">
<head>
<meta charset="utf-8">
<title>RKW Holdings – Business Card</title>
<link rel="stylesheet" href="https://fonts.googleapis.com/css2?family=Lato:wght@300;400;700&display=swap">
<style>
  :root {
    --brand-blue: #1776ae;
    --charcoal: #4d4e50;
    --ink: #1c1c1c;
    --pale-blue: #a4b6d8;
    --paper: #ffffff;
  }
  html, body {
    margin: 0;
    padding: 0;
    overflow: hidden;
    background: var(--paper);
  }
  .canvas {
    position: relative;
    width: 1080px;
    height: 1200px;
    overflow: hidden;
    background: var(--paper);
    font-family: "Lato", sans-serif;
  }
  .band {
    position: absolute;
    height: 27px;
  }
  .band--front-top    { left: 143px; width: 818px; top: 86px;   background: var(--charcoal); }
  .band--front-bottom { left: 143px; width: 818px; top: 527px;  background: var(--brand-blue); }
  .band--back-top     { left: 552px; width: 409px; top: 593px;  background: var(--charcoal); }
  .band--back-bottom  { left: 143px; width: 409px; top: 1034px; background: var(--brand-blue); }

  .brand-mark {
    position: absolute;
    left: 497px;
    top: 212px;
    width: 110px;
    height: 110px;
    background: var(--brand-blue);
  }
  .brand-name {
    position: absolute;
    left: 0;
    top: 360px;
    width: 1080px;
    text-align: center;
    font-size: 50px;
    font-weight: 400;
    letter-spacing: 1px;
    color: var(--charcoal);
    margin: 0;
  }
  .brand-tagline {
    position: absolute;
    left: 0;
    top: 469px;
    width: 1080px;
    text-align: center;
    font-size: 19px;
    font-weight: 300;
    color: var(--charcoal);
    margin: 0;
    letter-spacing: 0.3px;
  }

  .name-tab {
    position: absolute;
    left: 143px;
    top: 669px;
    width: 26px;
    height: 53px;
    background: var(--charcoal);
    border-radius: 0 12px 12px 0;
  }
  .person-name {
    position: absolute;
    left: 200px;
    top: 660px;
    margin: 0;
    font-size: 36px;
    font-weight: 700;
    color: var(--brand-blue);
    letter-spacing: -0.5px;
  }
  .person-role {
    position: absolute;
    left: 201px;
    top: 703px;
    margin: 0;
    font-size: 20px;
    font-weight: 300;
    color: var(--ink);
  }

  .contact-list {
    position: absolute;
    left: 201px;
    top: 768px;
    margin: 0;
    padding: 0;
    list-style: none;
  }
  .contact-item {
    display: flex;
    align-items: center;
    height: 39px;
    margin-bottom: 21px;
    font-size: 19px;
    color: var(--ink);
  }
  .contact-icon {
    width: 39px;
    height: 39px;
    flex: none;
    margin-right: 11px;
  }

  .back-decoration {
    position: absolute;
    left: 632px;
    top: 710px;
    width: 260px;
    height: 260px;
    background: var(--pale-blue);
    opacity: 0.55;
  }
</style>
</head>
<body>
<main class="canvas">
  <section class="card card--front">
    <div class="band band--front-top"></div>
    <div class="brand-mark"></div>
    <h1 class="brand-name">RKW Holdings</h1>
    <p class="brand-tagline">Real Estate Investment Fund</p>
    <div class="band band--front-bottom"></div>
  </section>

  <section class="card card--back">
    <div class="band band--back-top"></div>
    <div class="name-tab"></div>
    <h2 class="person-name">Marcus Olvane</h2>
    <p class="person-role">Owner</p>

    <ul class="contact-list">
      <li class="contact-item">
        <svg class="contact-icon" viewBox="0 0 40 40" aria-hidden="true">
          <circle cx="20" cy="20" r="20" fill="var(--brand-blue)"/>
          <path d="M13 11 l4 -1 l3 6 l-2.5 2 q2 4.5 6.5 6.5 l2 -2.5 l6 3 l-1 4 q-1.5 2 -4 1.5 q-9 -2.5 -14.5 -14 q-0.5 -3 0.5 -5.5z" fill="#fff"/>
        </svg>
        (917) 482-0657
      </li>
      <li class="contact-item">
        <svg class="contact-icon" viewBox="0 0 40 40" aria-hidden="true">
          <circle cx="20" cy="20" r="20" fill="var(--brand-blue)"/>
          <rect x="10" y="13" width="20" height="14" rx="1.5" fill="none" stroke="#fff" stroke-width="2"/>
          <path d="M10 14 L20 22 L30 14 M10 27 L17 20 M30 27 L23 20" fill="none" stroke="#fff" stroke-width="2"/>
        </svg>
        marcus@rkwholdings-example.com
      </li>
      <li class="contact-item">
        <svg class="contact-icon" viewBox="0 0 40 40" aria-hidden="true">
          <circle cx="20" cy="20" r="20" fill="var(--brand-blue)"/>
          <circle cx="20" cy="20" r="10.5" fill="none" stroke="#fff" stroke-width="2"/>
          <path d="M9.5 20 H30.5 M20 9.5 Q14 20 20 30.5 M20 9.5 Q26 20 20 30.5" fill="none" stroke="#fff" stroke-width="1.8"/>
        </svg>
        www.rkwholdings-example.com
      </li>
      <li class="contact-item">
        <svg class="contact-icon" viewBox="0 0 40 40" aria-hidden="true">
          <circle cx="20" cy="20" r="20" fill="var(--brand-blue)"/>
          <path d="M20 8 a7 7 0 0 1 7 7 q0 5 -7 11 q-7 -6 -7 -11 a7 7 0 0 1 7 -7z" fill="#fff"/>
          <circle cx="20" cy="15" r="2.8" fill="var(--brand-blue)"/>
          <path d="M11 30 H29" stroke="#fff" stroke-width="2"/>
        </svg>
        418, 9th Street, Brooklyn NY 11218
      </li>
    </ul>

    <div class="back-decoration"></div>
    <div class="band band--back-bottom"></div>
  </section>
</main>
</body>
</html>
```